We need a poster design for "KEVO Sports Night" events. The events have been around for 3 years and we hope the poster will give a sense of vibrant and active designs. It is more to a community event with teamwork and fun.

I have uploaded a past event poster just FYI.

Target Market(s)

Community, Family

Industry/Entity Type

Non Profit

Logo Text

KEVO Sports Night

Requirements
Must have
• KEVO Sports Night
• Organiser: KEVO Sydney
• Date: 25/11/2017
• Time: 4:00pm
• Venue: Wendamere Park
• Facebook: kevosport

```html
<!DOCTYPE html>
<html lang="en">
<head>
<meta charset="utf-8">
<title>KEVO Sports Night</title>
<link rel="stylesheet" href="https://fonts.googleapis.com/css2?family=Bebas+Neue&family=Montserrat:wght@400;600;700&display=swap">
<style>
  :root {
    --page: #ffffff;
    --sun: #fdc235;
    --chalk: #ffffff;
    --ink: #111111;
    --runner-dark: #2a2018;
    --runner-warm: #7a3a2a;
  }
  html, body {
    margin: 0;
    padding: 0;
    width: 1200px;
    height: 900px;
    overflow: hidden;
    background: var(--page);
  }
  .poster {
    position: absolute;
    left: 327px;
    top: 75px;
    width: 528px;
    height: 745px;
    background: var(--sun);
    overflow: hidden;
  }
  .title {
    position: absolute;
    left: 0;
    top: 0;
    width: 528px;
    height: 745px;
  }
  .title text {
    font-family: "Bebas Neue", "Oswald", sans-serif;
    fill: var(--chalk);
  }
  .time-box {
    position: absolute;
    left: 46px;
    top: 642px;
    width: 222px;
    height: 83px;
    background: var(--ink);
    color: var(--sun);
    font-family: "Bebas Neue", "Oswald", sans-serif;
  }
  .time-box .clock {
    position: absolute;
    left: 16px;
    top: 4px;
    font-size: 92px;
    line-height: 1;
    letter-spacing: 3px;
  }
  .time-box .meridiem {
    position: absolute;
    left: 165px;
    top: 6px;
    font-size: 38px;
    line-height: 1;
    letter-spacing: 1px;
  }
  .details {
    position: absolute;
    left: 287px;
    top: 640px;
    font-family: "Montserrat", sans-serif;
    color: var(--ink);
    line-height: 1;
  }
  .details .date {
    font-size: 25px;
    font-weight: 600;
    letter-spacing: 2px;
    margin: 0 0 8px;
  }
  .details .venue {
    font-size: 16.5px;
    font-weight: 400;
    margin: 0 0 13px;
  }
  .details .venue strong { font-weight: 700; }
  .details .organiser,
  .details .social {
    font-size: 12.5px;
    font-weight: 600;
    margin: 0 0 4px;
  }
</style>
</head>
<body>
  <main class="poster">
    <svg class="title" viewBox="0 0 528 745" aria-labelledby="event-name">
      <title id="event-name">KEVO Sports Night</title>
      <text x="43" y="270" font-size="350" textLength="455" lengthAdjust="spacingAndGlyphs">KEVO</text>
      <text x="43" y="435" font-size="207" textLength="455" lengthAdjust="spacingAndGlyphs">SPORTS</text>
      <text x="43" y="625" font-size="250" textLength="455" lengthAdjust="spacingAndGlyphs">NIGHT</text>
      <defs>
        <linearGradient id="runner-tone" x1="0" y1="0" x2="0" y2="1">
          <stop offset="0" stop-color="var(--runner-warm)"/>
          <stop offset="1" stop-color="var(--runner-dark)"/>
        </linearGradient>
      </defs>
      <rect class="runner-photo" x="388" y="472" width="86" height="162" rx="6"
            fill="url(#runner-tone)" opacity="0.85"
            role="img" aria-label="Photo from above of a sprinter casting a long shadow across the title"/>
    </svg>

    <div class="time-box">
      <span class="clock">4:00</span><span class="meridiem">PM</span>
    </div>

    <div class="details">
      <p class="date">25 | 11 | 2017</p>
      <p class="venue">VENUE <strong>WENDAMERE PARK</strong></p>
      <p class="organiser">ORGANIZED BY KEVO SYDNEY</p>
      <p class="social">FB.COM/KEVOSPORT</p>
    </div>
  </main>
</body>
</html>
```